Web Design Project

I'm looking for a major redesign for my existing photographic art website: www.brightmeadowart.com. Here are my complaints about the current layout: 1) It looks unsophisticated (we will, of course, delete the "sale" banner; 2) the images are vastly too small when displayed in the gallery; 3) I'm not wild about the navigation; 4) the Flash has got to go; 4) there has to be an easy way to significantly enlarge the photos for viewing; 5) the copy is a bit over the top - we will be rewriting it. Other than that, it's a good site :)

The market for the photography is principally commercial applications - interior designers, etc. who are concerned with how these images will look in hospitals, office buildings, etc. The leading competitor in this space has a much better site: www.walterpriske.com. Another site worth viewing is: www.torvelt.com. This site is much more akin to my site.

We will be reducing the number of photos available. Total count will be approximately 400. The largest collection will be the "petal study" - close up photography of flowers, plants, etc.

I am amazed at the quality of the submissions - which has made the selection process very, very difficult. Each of you should be very proud of the quality of work you produce. Beyond this web-site, which is a "sideline" for me, I run a large marketing organization....and have shared these submissions with all of my colleagues who were duly impressed. Hopefully we will have an opportunity to work with you on a differentp project!

Thank you!!!
Mark

```html
<!DOCTYPE html>
<html lang="en">
<head>
<meta charset="utf-8">
<title>Bright Meadow — Photography by Mark Halden</title>
<link href="https://fonts.googleapis.com/css2?family=PT+Sans:ital,wght@0,400;0,700;1,400;1,700&family=Noto+Sans:wght@400&display=swap" rel="stylesheet">
<style>
:root{
  --ink:#000;
  --paper:#fff;
  --panel:rgba(8,4,2,.72);
  --panel-head:rgba(45,22,6,.9);
  --accent:#e8945a;
  --peach:#f4d7b6;
  --card:rgba(255,245,235,.62);
  --btn:#4a4643;
  --green:#6cc12e;
  --footer:rgba(10,6,3,.82);
  --footer-link:#8c4a1c;
}
*{margin:0;padding:0;box-sizing:border-box}
html,body{width:1200px;height:1053px;overflow:hidden}
body{position:relative;font-family:"Noto Sans",Verdana,sans-serif;color:var(--paper)}
.backdrop{position:absolute;inset:0;
  background:
    radial-gradient(ellipse 60% 30% at 20% 72%,rgba(255,214,120,.75),transparent 70%),
    linear-gradient(180deg,#3a2412 0%,#7a4a1e 20%,#b87a30 45%,#e0a850 68%,#6a4222 82%,#3c2614 92%,#c99a5c 100%);}
.ui-abs{position:absolute}
.brand-mark{left:169px;top:38px;width:84px;height:84px;background:var(--ink)}
.brand-name{left:107px;top:128px;font:400 28px/1 "PT Sans",sans-serif;color:var(--paper);width:220px;text-align:center}
.nav a{position:absolute;left:105px;height:48px;background:var(--ink);color:var(--paper);
  font:italic 400 20px/48px "PT Sans",sans-serif;padding-left:32px;text-decoration:none}
.nav a.active{background:var(--paper);color:var(--ink)}
.side-title{left:104px;font:italic 700 28px/1 "PT Sans",sans-serif}
.side-title.order{top:498px;color:var(--peach)}
.side-title.call{top:808px;color:var(--ink)}
.card{position:absolute;left:105px;width:203px;background:var(--card);border-radius:3px}
.btn{position:absolute;height:26px;background:var(--btn);border-radius:3px;color:#fff;
  font:400 12.5px/26px "Noto Sans",sans-serif;text-align:center}
.card p{position:absolute;left:16px;top:66px;width:160px;color:#222;font-size:12.5px;line-height:19px}
.search-field{position:absolute;left:20px;top:18px;width:134px;height:26px;background:#2e2c2a;border-radius:4px 0 0 4px;
  font-size:12.5px;line-height:26px;padding-left:16px;color:#ddd}
.search-go{position:absolute;left:154px;top:18px;width:26px;height:26px;background:var(--green);border:1px solid #3d7a14;border-radius:0 3px 3px 0}
.phone{color:#111;font:400 24px/65px "Noto Sans",sans-serif;text-align:center}
.main{left:436px;top:29px;width:676px;height:940px;background:var(--panel)}
.main-head{position:absolute;left:0;top:0;width:100%;height:58px;background:var(--panel-head)}
.main-title{position:absolute;left:28px;top:15px;font:italic 700 20px/1 "PT Sans",sans-serif;color:var(--accent)}
.divider{position:absolute;left:267px;top:16px;width:1px;height:26px;background:#c9a88a}
.tagline{position:absolute;left:276px;top:22px;font-size:11px}
.close{position:absolute;left:642px;top:13px}
.sale{position:absolute;top:76px;width:100%;text-align:center;font:italic 400 20px/1 "PT Sans",sans-serif}
.sale-note{position:absolute;top:114px;width:100%;text-align:center;font-size:12px}
.feature{position:absolute;left:84px;top:156px;width:515px;height:642px;background:var(--paper);padding:8px}
.feature-img{width:100%;height:100%;background:radial-gradient(circle at 48% 48%,#f3b23a 0,#d04fa0 12%,#b867e0 28%,#8a3fb8 42%,#1a0a20 58%,#000 75%)}
.intro{position:absolute;left:29px;top:801px;width:620px;font-size:12.5px;line-height:18.2px}
.footer{left:0;top:987px;width:1200px;height:66px;background:var(--footer)}
.footer-mark{position:absolute;left:107px;top:8px;width:50px;height:50px;background:var(--ink)}
.copyright{position:absolute;left:173px;top:24px;font-size:13px}
.footer-nav{position:absolute;right:88px;top:24px;font-size:13px;color:var(--footer-link)}
</style>
</head>
<body>
<div class="backdrop" role="img" aria-label="Sunset over a rocky beach with palm trees silhouetted against an orange sky"></div>

<div class="ui-abs brand-mark"></div>
<div class="ui-abs brand-name">Bright Meadow</div>

<nav class="nav">
  <a class="active" style="top:207px;width:271px">Gallery</a>
  <a style="top:262px;width:217px">Architects / Designers</a>
  <a style="top:318px;width:237px">About The Artist</a>
  <a style="top:373px;width:287px">Ordering Information</a>
  <a style="top:429px;width:228px">Contact&nbsp; Us</a>
</nav>

<div class="ui-abs side-title order">To Order</div>
<div class="card" style="top:522px;height:115px">
  <div class="btn" style="left:12px;top:27px;width:87px">Login</div>
  <div class="btn" style="left:102px;top:27px;width:87px">SignUp</div>
  <p>You have 0 item(s) in your cart.</p>
</div>
<div class="card" style="top:650px;height:73px">
  <div class="btn" style="left:12px;top:27px;width:87px">Lightbox</div>
  <div class="btn" style="left:102px;top:27px;width:87px">
    <svg width="18" height="14" viewBox="0 0 18 14" style="vertical-align:-2px;margin-right:6px"><path d="M1 1h3l2 8h9l2-6H5" fill="none" stroke="#fff" stroke-width="1.5"/><circle cx="7" cy="12" r="1.4" fill="#fff"/><circle cx="14" cy="12" r="1.4" fill="#fff"/></svg>Cart</div>
</div>
<div class="card" style="top:734px;height:64px">
  <div class="search-field">Search</div>
  <div class="search-go"><svg width="24" height="24" viewBox="0 0 24 24"><circle cx="11" cy="10" r="4.5" fill="none" stroke="#fff" stroke-width="2"/><path d="M14 13l4 4" stroke="#fff" stroke-width="2.4"/></svg></div>
</div>
<div class="ui-abs side-title call">Call Us</div>
<div class="card phone" style="top:834px;height:63px">877-555-0142</div>

<main class="ui-abs main">
  <header class="main-head">
    <div class="main-title">Photography by Mark Halden</div>
    <div class="divider"></div>
    <div class="tagline">Photography that transcends our normal view of the world</div>
    <svg class="close" width="18" height="18" viewBox="0 0 18 18"><path d="M2 2l14 14M16 2L2 16" stroke="#9a8a7c" stroke-width="1.6"/></svg>
  </header>
  <div class="sale">SALE! All photographs 30% off.</div>
  <div class="sale-note">Discount will be applied automatically in the shopping cart as part of the ordering process.</div>
  <figure class="feature"><div class="feature-img" role="img" aria-label="Close-up of a purple water lily with a golden centre on a black background"></div></figure>
  <p class="intro">Welcome to the world of Mark Halden. Come in and enjoy a place where stunning horizons meet glorious skies. A place where light and shade dance together in flawless rhythm. Come in and discover a world of photography that begins and ends with a shutter. Come in, relax and browse the gallery. You are about to experience some of the most inspiring and enchanting imagery the world has to offer.</p>
</main>

<footer class="ui-abs footer">
  <div class="footer-mark"></div>
  <div class="copyright">© 2010 Halden Photography</div>
  <div class="footer-nav">Gallery | Architects/Designers | About the Artist | Ordering Information | Contact Us</div>
</footer>
</body>
</html>
```